Herbalist's Pain Cream WIX Website Redesign

I need a complete WIX website redesign! I am an herbalist and I'm relaunching my company, starting with a pain cream as the flagship product. My natural pain relief cream is composed of 6 active botanicals, uses all natural preservatives and provides pain relief within 1 minute! I have a new label design that reflects the high quality of this product and its ingredients. I have the content written and a rough website outline. I want the new website to match the color scheme of the label, and to show the quality of the product. (Logo uploaded is older color scheme. See New Label upload for updated color scheme.) I will be launching more products in the future, but the current content is for 1 flagship product. I want a high quality, earthy/ natural, botanical medicine feel. SEO phrase "Natural Pain Relief Cream" Old website is up again, for pictures: www.fennowildroot.com

Target Market(s)

Middle to later aged women, Same for Men, but usually introduced by woman in their life

Industry/Entity Type

Botanical Supplement

Coding

Coded - Design and coding required

Number of Pages Required

5+ page

Colors
0054AA
0677BA
7BADD7
CADEEF
E8F1F8

Requirements
Must have
• Homepage, About, Ingredients, Shop, Contact Us
Nice to have
• FAQ section, maybe graphics to highlight unique elements

```html
<!DOCTYPE html>
<html lang="en">
<head>
<meta charset="utf-8">
<title>Fenno Wildroot – Natural Pain Relief Cream</title>
<link href="https://fonts.googleapis.com/css2?family=Poppins:wght@300;400;500;600;700&display=swap" rel="stylesheet">
<style>
:root{
  --navy:#0054AA;
  --blue:#0677BA;
  --sky:#7BADD7;
  --mist:#CADEEF;
  --ice:#E8F1F8;
  --ink:#1b1b1b;
  --text:#333;
  --white:#fff;
}
*{margin:0;padding:0;box-sizing:border-box}
html,body{width:1200px;height:4983px;overflow:hidden}
body{font-family:'Poppins',sans-serif;color:var(--text);background:var(--white);position:relative}
.abs{position:absolute}
.btn{position:absolute;display:inline-flex;align-items:center;gap:12px;background:var(--navy);color:var(--white);font-weight:600;font-size:14px;border-radius:30px;padding:0 16px 0 26px;height:46px;text-decoration:none}
.btn .arr{width:20px;height:20px;border-radius:50%;background:var(--white);display:flex;align-items:center;justify-content:center}
.btn.light{background:var(--white);color:var(--navy)}
.btn.light .arr{background:var(--navy)}
.photo{position:absolute;border-radius:50%}

/* top bar */
.topbar{top:0;left:0;width:1200px;height:40px;background:var(--navy);color:var(--white);font-size:13px}
.topbar .mail{position:absolute;left:168px;top:11px;display:flex;gap:8px;align-items:center}
.social{position:absolute;display:flex;gap:12px}
.social span{width:18px;height:18px;border-radius:50%;background:currentColor;display:block}
.topbar .social{right:156px;top:11px;color:var(--white)}

/* header */
.brand{position:absolute;display:flex;align-items:center;gap:12px;color:var(--blue);font-weight:500;font-size:24px;letter-spacing:.5px}
.brand .dot{width:40px;height:40px;border-radius:50%;background:var(--navy)}
.nav{position:absolute;top:92px;left:478px;display:flex;gap:36px;font-size:13px;font-weight:500;color:var(--ink)}
.nav .on{border-bottom:2px solid var(--navy);padding-bottom:8px}

/* hero */
.hero-kicker{left:124px;top:244px;color:var(--navy);font-weight:600;font-size:27px}
.hero-title{left:124px;top:278px;font-weight:700;font-size:50px;line-height:1.2;color:var(--ink)}
.hero-sub{left:124px;top:418px;font-size:13px}

/* features */
.features{top:735px;left:0;width:1200px;height:560px;background:#F2F7FB}
.feature{position:absolute;top:0;width:300px;text-align:center}
.feature .art{width:190px;height:190px;margin:44px auto 0;border-radius:50%;background:var(--mist);position:relative}
.feature .art i{position:absolute;left:80px;top:40px;width:30px;height:30px;border-radius:50%;background:var(--blue);color:#fff;font-style:normal;font-size:14px;line-height:30px}
.feature .art b{position:absolute;left:45px;top:85px;width:100px;height:100px;border-radius:50%;background:var(--ice);border:2px dashed var(--blue)}
.feature h3{margin-top:95px;font-size:16px;font-weight:600;color:var(--ink);line-height:1.25}
.feature p{margin-top:18px;font-size:13px;line-height:1.55}

/* feel */
.feel{top:1316px;left:0;width:1200px;height:580px;background:var(--ice)}
.feel h2{position:absolute;left:598px;top:70px;font-size:33px;font-weight:600;line-height:1.25;color:var(--ink)}
.feel .lead{position:absolute;left:598px;top:172px;width:500px;font-size:13px;line-height:1.55}
.steps{position:absolute;left:598px;top:256px;display:flex;gap:22px}
.step{width:112px;height:130px;background:var(--mist);border-radius:10px;position:relative;text-align:center;font-weight:600;font-size:16px;color:var(--ink)}
.step .ic{width:78px;height:78px;border-radius:50%;background:var(--white);border:2px dashed var(--blue);margin:-14px auto 0}
.step span{display:block;margin-top:22px}
.feel .tag{position:absolute;left:600px;top:414px;font-size:19px;font-weight:500;color:var(--ink)}

/* herbs */
.herbs{top:1896px;left:0;width:1200px;height:504px;background:linear-gradient(90deg,var(--navy),var(--blue))}
.card{position:absolute;left:180px;top:97px;width:840px;height:439px;background:var(--ice);border:2px solid var(--mist);border-radius:14px}
.card .corner{position:absolute;left:12px;top:12px;width:0;height:0;border-top:22px solid var(--navy);border-right:22px solid transparent}
.card h2{position:absolute;left:40px;top:28px;width:330px;font-size:33px;line-height:1.25;font-weight:600;color:var(--ink)}
.card h2 em{font-style:normal;font-weight:300}
.card .copy{position:absolute;left:404px;top:28px;width:380px;font-size:13px;line-height:1.55}
.card .copy p+p{margin-top:16px}

/* expertise */
.expert h2{position:absolute;left:116px;top:2572px;font-size:34px;line-height:1.25;font-weight:600;color:var(--ink)}
.expert p{position:absolute;left:116px;top:2680px;width:480px;font-size:13px;line-height:1.55}

/* testimonials */
.testi{top:2941px;left:0;width:1200px;height:620px;background:var(--ice)}
.testi h2{position:absolute;top:125px;width:100%;text-align:center;font-size:33px;font-weight:600;color:var(--ink)}
.testi h3{position:absolute;top:185px;width:100%;text-align:center;font-size:33px;font-weight:300;color:var(--ink)}
.testi blockquote{position:absolute;left:196px;top:260px;width:780px;text-align:center;font-size:13px;line-height:1.6;color:#666}
.testi .nav-dot{position:absolute;top:302px;width:38px;height:38px;border-radius:50%;background:var(--navy);display:flex;align-items:center;justify-content:center}
.testi .avatar{position:absolute;left:550px;top:450px;width:34px;height:34px;border-radius:50%;background:var(--sky)}
.testi .stars{position:absolute;top:497px;width:100%;text-align:center;color:#f0cc52;font-size:14px;letter-spacing:6px}
.testi .who{position:absolute;top:525px;width:100%;text-align:center;font-size:19px;color:var(--ink)}
.testi .bar{position:absolute;left:545px;top:566px;width:44px;height:3px;background:var(--blue)}

/* faq */
.faq-title{top:3632px;width:1200px;text-align:center;font-size:33px;font-weight:600;color:var(--ink)}
.faq{position:absolute;left:116px;width:968px;height:50px;border-radius:4px;background:var(--ice);display:flex;align-items:center;justify-content:space-between;padding:0 34px 0 38px;font-size:16px;font-weight:600;color:var(--ink)}
.faq.open{background:var(--navy);color:var(--white)}
.faq.alt{background:var(--mist)}
.faq-answer{left:156px;top:3778px;width:890px;font-size:11px;line-height:1.7;color:#666}

/* cta */
.cta{left:116px;top:4203px;width:968px;height:272px;border-radius:18px;background:linear-gradient(90deg,var(--navy),var(--blue) 50%,var(--navy));text-align:center;color:var(--white)}
.cta h2{position:absolute;top:82px;width:100%;font-size:24px;font-weight:600;line-height:1.3}

/* footer */
.footer{top:4644px;left:0;width:1200px;height:339px;background:var(--ice)}
.footer h4{position:absolute;font-size:18px;font-weight:600;color:var(--ink)}
.footer ul{position:absolute;left:490px;top:98px;list-style:none;font-size:12px;line-height:28px;color:var(--ink)}
.footer ul li::before{content:"•";margin-right:8px}
.contact{position:absolute;left:116px;font-size:13px;display:flex;gap:20px;align-items:center;color:var(--ink)}
.sub{position:absolute;left:774px;top:104px;width:305px;height:42px;display:flex;border-radius:4px;overflow:hidden}
.sub span{flex:1;background:var(--white);font-size:12px;color:#999;padding:13px 14px;border:1px solid var(--mist)}
.sub b{width:92px;background:var(--navy);color:var(--white);font-size:13px;font-weight:600;text-align:center;line-height:42px}
.footer .rule{position:absolute;left:116px;top:276px;width:968px;height:1px;background:#bbb}
.footer .copy{position:absolute;top:300px;width:100%;text-align:center;font-size:13px;color:var(--ink)}
</style>
</head>
<body>

<header>
  <div class="abs topbar">
    <div class="mail"><svg width="14" height="11" viewBox="0 0 14 11"><rect x="0.5" y="0.5" width="13" height="10" rx="1" fill="#fff"/><path d="M1 1l6 5 6-5" stroke="#0054AA" fill="none"/></svg>info@fennowildroot.com</div>
    <div class="social"><span></span><span></span><span></span><span></span></div>
  </div>
  <div class="brand" style="left:114px;top:76px"><span class="dot"></span>FENNO WILDROOT</div>
  <nav class="nav"><span class="on">HOME</span><span>ABOUT</span><span>INGREDIENTS</span><span>SHOP</span><span>FAQ</span></nav>
  <a class="btn" style="left:900px;top:76px;height:42px;font-size:13px">Contact Us <span class="arr"><svg width="10" height="10" viewBox="0 0 10 10"><path d="M3 1l4 4-4 4" stroke="#0054AA" stroke-width="2" fill="none"/></svg></span></a>
</header>

<section class="hero">
  <div class="abs hero-kicker">WELCOME TO</div>
  <h1 class="abs hero-title">FENNO WILDROOT<br>REMEDIES,</h1>
  <p class="abs hero-sub">Where the wisdom of nature meets the art of healing.</p>
  <a class="btn" style="left:124px;top:466px">Buy Now <span class="arr"><svg width="10" height="10" viewBox="0 0 10 10"><path d="M3 1l4 4-4 4" stroke="#0054AA" stroke-width="2" fill="none"/></svg></span></a>
  <div class="photo" role="img" aria-label="Woman jogging with pain relief cream jar and leaf decoration" style="left:670px;top:195px;width:360px;height:360px;background:radial-gradient(circle,var(--mist),var(--sky))"></div>
  <div class="abs" role="img" aria-label="Jar of natural pain relief cream" style="left:612px;top:410px;width:180px;height:170px;border-radius:18px;background:linear-gradient(180deg,#dfe8f3,#b9cde3)"></div>
  <div class="photo" role="img" aria-label="Close-up of back pain" style="left:665px;top:182px;width:120px;height:120px;border:5px solid #fff;background:linear-gradient(135deg,#f2c7b8,#d97a6a)"></div>
  <div class="photo" role="img" aria-label="Woman stretching in yoga pose by the sea" style="left:950px;top:440px;width:170px;height:170px;border:5px solid #fff;background:linear-gradient(180deg,#cfe0ee,#8fa9bd)"></div>
  <svg class="abs" style="left:0;top:620px" width="1200" height="130" viewBox="0 0 1200 130" aria-hidden="true">
    <path d="M0 70 C300 20 500 45 760 55 C950 62 1100 60 1200 55 L1200 130 L0 130Z" fill="#F2F7FB"/>
    <path d="M0 70 C250 30 450 40 700 48 C900 54 1080 40 1200 40 L1200 60 C1050 58 900 70 700 66 C450 60 250 50 0 72Z" fill="#7BADD7"/>
    <path d="M0 72 C200 40 420 35 620 45 C420 45 220 55 0 78Z" fill="#0054AA"/>
  </svg>
</section>

<section class="abs features">
  <div class="feature" style="left:119px"><div class="art" role="img" aria-label="Molecule icon on leaf ornament"><i>1</i><b></b></div><h3>EXPERTLY CRAFTED<br>FORMULA</h3><p>Formulated by an herbalist<br>with over a decade of<br>clinical experience.</p></div>
  <div class="feature" style="left:450px"><div class="art" role="img" aria-label="Bowl of botanicals icon on leaf ornament"><i>2</i><b></b></div><h3>FAST-ACTING<br>INGREDIENTS</h3><p>With nature's power at the forefront,<br>our 6 active botanicals deliver<br>almost instant relief.</p></div>
  <div class="feature" style="left:779px;width:330px"><div class="art" role="img" aria-label="Hand holding flower icon on leaf ornament"><i>3</i><b></b></div><h3>NURTURING<br>TOUCH</h3><p>Not only does our natural pain relief cream<br>alleviate discomfort, but it also nourishes and<br>rejuvenates your skin.</p></div>
</section>

<svg class="abs" style="left:0;top:1250px" width="1200" height="70" viewBox="0 0 1200 70" aria-hidden="true"><path d="M0 0 H1200 V25 C900 60 700 20 450 30 C250 38 120 60 0 50Z" fill="#F2F7FB"/><path d="M0 50 C120 60 250 38 450 30 C700 20 900 60 1200 25 V70 H0Z" fill="#E8F1F8"/></svg>

<section class="abs feel">
  <div class="photo" role="img" aria-label="Woman holding sore knee" style="left:200px;top:40px;width:330px;height:330px;background:radial-gradient(circle,#d7e5f2,var(--mist))"></div>
  <div class="abs" role="img" aria-label="Seated woman in pink top clutching her knee" style="left:150px;top:70px;width:440px;height:330px;border-radius:40px;background:linear-gradient(135deg,#e9b8b6,#333 70%,#222);opacity:.85"></div>
  <div class="photo" role="img" aria-label="Close-up of wrist pain" style="left:448px;top:100px;width:115px;height:115px;border:5px solid #fff;background:linear-gradient(135deg,#f1d3c5,#c97b6b)"></div>
  <div class="photo" role="img" aria-label="Lower back pain highlighted" style="left:130px;top:325px;width:165px;height:165px;border:5px solid #fff;background:linear-gradient(135deg,#e6a58e,#c44c3c)"></div>
  <h2>FEEL THE DIFFERENCE IN<br>JUST 1 MINUTE!</h2>
  <p class="lead">Whether you're overcoming the strains of daily life or the demands of an active lifestyle, our natural pain relief cream is your go-to solution for quick relief</p>
  <div class="steps">
    <div class="step"><div class="ic" role="img" aria-label="Apply icon"></div><span>APPLY</span></div>
    <div class="step"><div class="ic" role="img" aria-label="Relax icon"></div><span>RELAX</span></div>
    <div class="step"><div class="ic" role="img" aria-label="Reclaim icon"></div><span>RECLAIM</span></div>
  </div>
  <div class="tag">Your Day—Experience Relief Today!</div>
  <a class="btn" style="left:598px;top:478px;height:42px;font-size:13px">Buy Now <span class="arr"><svg width="10" height="10" viewBox="0 0 10 10"><path d="M3 1l4 4-4 4" stroke="#0054AA" stroke-width="2" fill="none"/></svg></span></a>
</section>

<section class="abs herbs">
  <div class="abs" role="img" aria-label="Botanical leaf line drawing" style="left:0;top:0;width:170px;height:500px;background:linear-gradient(180deg,rgba(255,255,255,.12),rgba(255,255,255,0))"></div>
  <div class="abs" role="img" aria-label="Botanical leaf line drawing" style="right:0;top:60px;width:170px;height:400px;background:linear-gradient(180deg,rgba(255,255,255,.12),rgba(255,255,255,0))"></div>
  <div class="card">
    <span class="corner"></span>
    <h2>WE USE HERBS HARVESTED FROM THE WILD AND FROM THE FARM, <em>TO DELIVER A POTENT NATURAL HEALING EXPERIENCE.</em></h2>
    <div class="copy">
      <p>At Fenno Wildroot, we understand that when discomfort strikes, you seek swift and effective relief. That's why it is important to use the most powerful botanical ingredients in our natural pain relief cream. Each ingredient reflects a commitment to quality and efficacy, harnessing the powerful properties of nature's finest ingredients. From the strongest Yarrow cultivar on earth, grown on a 500 year old farm in Bulgaria, to a wild Arnica species harvested for us in the Cascade Mountains, we use our most powerful plant allies to ensure you get the relief you need</p>
      <p>Try our <b>natural pain relief cream</b> and let the calming embrace of nature guide you toward a place of comfort and vitality.</p>
    </div>
    <a class="btn" style="left:404px;top:362px;height:42px;font-size:13px">Explore the Ingredients <span class="arr"><svg width="10" height="10" viewBox="0 0 10 10"><path d="M3 1l4 4-4 4" stroke="#0054AA" stroke-width="2" fill="none"/></svg></span></a>
  </div>
</section>

<section class="expert">
  <h2>EXPERIENCE THE DIFFERENCE<br>THAT EXPERTISE MAKES!</h2>
  <p>Meet Tomas, the creator of Fenno Wildroot. Inspired by his personal journey to heal his chronic pain, he devoted his life to studying medicinal plants and how to harness their healing abilities to improve the lives of others. As a trained herbalist, botanical medicine researcher and supplement formulator, let Tomas's expertise guide you back to health and wellness. Discover the restorative power of herb-based solutions at Fenno Wildroot!</p>
  <a class="btn" style="left:116px;top:2848px;height:42px;font-size:13px">Read More About Tomas <span class="arr"><svg width="10" height="10" viewBox="0 0 10 10"><path d="M3 1l4 4-4 4" stroke="#0054AA" stroke-width="2" fill="none"/></svg></span></a>
  <div class="photo" role="img" aria-label="Joyful woman with arms raised" style="left:662px;top:2560px;width:390px;height:390px;background:radial-gradient(circle,var(--mist),var(--sky))"></div>
  <div class="photo" role="img" aria-label="Close-up of sore shoulder" style="left:950px;top:2548px;width:120px;height:120px;border:5px solid #fff;background:linear-gradient(135deg,#f1cfc0,#d0776a)"></div>
  <div class="photo" role="img" aria-label="Close-up of sore heel" style="left:618px;top:2762px;width:160px;height:160px;border:5px solid #fff;background:linear-gradient(135deg,#f3d8c7,#c06a5c)"></div>
</section>

<section class="abs testi">
  <h2>TESTIMONIALS</h2>
  <h3>This Is Magical Pain Cream</h3>
  <span class="nav-dot" style="left:124px"><svg width="12" height="12" viewBox="0 0 10 10"><path d="M7 1L3 5l4 4" stroke="#fff" stroke-width="2" fill="none"/></svg></span>
  <span class="nav-dot" style="left:1005px"><svg width="12" height="12" viewBox="0 0 10 10"><path d="M3 1l4 4-4 4" stroke="#fff" stroke-width="2" fill="none"/></svg></span>
  <blockquote>"Tomas Fenno is a life changer! Believe me when I say it, this pain cream is pure magic! Between my husband and I, we have racked up the itises through car wrecks, bad luck, and growing older. We've taken the pills and tried the supplement. I've guinea pigged us both trying to make my own plant based pain reliever oils and creams because nothing was working that wasn't causing other problems. But I'm a total amateur....so...eh... 😄 Tomas is a masterful REAL clinical herbalist—not the mail order kind. Lol. His plant healing knowledge is unending, and he's changed the lives of so many by giving us our health back! You won't find any other cream better than this expertly crafted jar of heavenly RELIEF! Go read his bio, and the list of ingredients. Be mind blown! THANK YOU!"</blockquote>
  <div class="avatar" role="img" aria-label="Reviewer portrait"></div>
  <div class="stars">★★★★★</div>
  <div class="who">Maren L. Birmingham, AL</div>
  <div class="bar"></div>
</section>

<section class="faq-block">
  <h2 class="abs faq-title">Frequntly Asked Question</h2>
  <div class="faq open" style="top:3715px">Does It Work? <svg width="14" height="9" viewBox="0 0 14 9"><path d="M1 1l6 6 6-6" stroke="#fff" stroke-width="2" fill="none"/></svg></div>
  <p class="abs faq-answer">Absolutely! You Will Start To Feel Relief Within 1 Minute. After 15 Minutes You Will Feel Its Full Effects. At Fenno Wildroot, We Stand By The Effectiveness Of Our Pain Cream, Which Is Truly More Than Just A Product—It's A Carefully Crafted Solution Born From Clinical Experience And Expertise.</p>
  <div class="faq alt" style="top:3840px">Whois This Natural Pain Relief Cream For? <svg width="14" height="9" viewBox="0 0 14 9"><path d="M1 1l6 6 6-6" stroke="#333" stroke-width="2" fill="none"/></svg></div>
  <div class="faq" style="top:3900px">Howdol Use It? <svg width="14" height="9" viewBox="0 0 14 9"><path d="M1 1l6 6 6-6" stroke="#333" stroke-width="2" fill="none"/></svg></div>
  <div class="faq" style="top:3960px">Howlong Is Your Pain Cream Good For? <svg width="14" height="9" viewBox="0 0 14 9"><path d="M1 1l6 6 6-6" stroke="#333" stroke-width="2" fill="none"/></svg></div>
  <div class="faq" style="top:4020px">Are Your Preservatives Natural? <svg width="14" height="9" viewBox="0 0 14 9"><path d="M1 1l6 6 6-6" stroke="#333" stroke-width="2" fill="none"/></svg></div>
  <div class="faq" style="top:4080px">What's Your Shipping And Delivery Times? <svg width="14" height="9" viewBox="0 0 14 9"><path d="M1 1l6 6 6-6" stroke="#333" stroke-width="2" fill="none"/></svg></div>
</section>

<section class="abs cta" role="img" aria-label="Woman in a field with botanical line drawings, tinted blue">
  <h2>Have more questions? We're just a message away! Embrace a<br>life free of discomfort—order your Pain Cream today</h2>
  <a class="btn light" style="left:405px;top:165px;height:42px;font-size:13px">Contact Us <span class="arr"><svg width="10" height="10" viewBox="0 0 10 10"><path d="M3 1l4 4-4 4" stroke="#fff" stroke-width="2" fill="none"/></svg></span></a>
</section>

<svg class="abs" style="left:0;top:4528px" width="1200" height="120" viewBox="0 0 1200 120" aria-hidden="true">
  <path d="M0 20 C250 40 500 80 800 60 C980 48 1100 30 1200 30 V120 H0Z" fill="#E8F1F8"/>
  <path d="M0 20 C250 40 500 70 800 50 C980 38 1100 15 1200 10 V32 C1100 35 980 55 800 65 C500 82 250 50 0 30Z" fill="#0054AA"/>
  <path d="M0 30 C250 50 500 82 800 65 C600 88 300 70 0 42Z" fill="#7BADD7"/>
</svg>

<footer class="abs footer">
  <div class="brand" style="left:114px;top:40px"><span class="dot"></span>FENNO WILDROOT</div>
  <div class="contact" style="top:146px"><svg width="14" height="14" viewBox="0 0 14 14"><path d="M3 1l2 3-1.5 1.5c1 2 2.5 3.5 4.5 4.5L9.5 8.5l3 2L11 13C5 12 2 8 1 3z" fill="#0054AA"/></svg>+1 (123) 456 7890</div>
  <div class="contact" style="top:182px"><svg width="14" height="11" viewBox="0 0 14 11"><rect x="0.5" y="0.5" width="13" height="10" rx="1" fill="#0054AA"/><path d="M1 1l6 5 6-5" stroke="#fff" fill="none"/></svg>hello@fennowildroot.com</div>
  <h4 style="left:482px;top:58px">QUICK LINKS</h4>
  <ul><li>HOME</li><li>ABOUT</li><li>INGREDIENTS</li><li>SHOP</li><li>FAQ</li></ul>
  <h4 style="left:774px;top:58px">SUBSCRIBE A NEWSLETTER</h4>
  <div class="sub"><span>Email Address</span><b>SUBMIT</b></div>
  <h4 style="left:774px;top:216px">SOCIAL MEDIA</h4>
  <div class="social" style="left:968px;top:220px;color:var(--navy)"><span></span><span></span><span></span><span></span></div>
  <div class="rule"></div>
  <div class="copy">© 2024 by Fenno Wildroot</div>
</footer>

</body>
</html>
```